Beauty Salon Industry - Web Design Project

zQuarta is a well-funded start up developing an Online Marketing Platform for small businesses in Europe.
We require a large number of high quality business web designs for our business website builder. Our business websites are seamlessly integrated into our Online Marketing systems and therefore it is important for designers to comply with our Design Guidelines.
This is our second contest and it will focus on the beauty salon industry. We will be running contents every 2-3 weeks for a new industry. Last month, we ran a contest for Builder website designs with 3 top prizes (plus £10 per variation) and we also paid out £25 per design for 20+ entries from designers who did not win the top prizes. So we encourage all entries!
We have included a wire frame this time to encourage you to be as creative as possible with your designs and layout while respecting the following guidelines:
1) You CAN change the layout as much as you like. If you think a vertical menu would look better, then use it. If you think the design would benefit from moving an element to a different location, then you can do that too.
2) You must include ALL the elements in the wire frame in your design.(e.g. latest 2 news entries, a testimonial, 1 gallery image, carousel etc...). Please make sure you have looked through the wire frame and know what is required. Entries that do not include all the elements will not qualify to win.
3) So remember, you CAN change the layout as much as you like but DO NOT remove any elements nor move them to a different page.
4) You may change the size and style of the carousel image. We would like to see as many variations of this as possible.
We are rewarding 3 prizes, and would like the winning designer to design the internal pages to the new design.
As always, if we think your designs could be incorporated into our system, but you do not win the competition, we will reward £25. Therefore, we encourage designers to submit as many designs as possible as we may award up to 25 designs.
Judging criteria : -
1) Visual Design
2) Layout must adhere to best practices and wireframe. If you decide to move elements around significantly please provide reason
3) Functional, informative and drives calls to action
Updates
As usual:
1st place = £350
2nd place = £250
3rd place = £150
Good luck!
Very happy with all the designs submitted so far, and will provide feedback ASAP.
We would like to see you try arranging the elements differently. So please try different navigation types and layouts.
Thanks
Morris
Prize funds for 1st place has been slightly increased.
Thanks
Morris
We have already had some amazing designs submitted. Thanks.
Remember to play with the layout of the elements and try designs with a carousel/slider that is in portrait not just in landscape.
Thanks everyone!
Morris
Hi everyone, we are really enjoying looking through the designs.
We have one NEW requirement. If you have used an image from http://www.frelik-example.com/ in your design, could you please replace it with another.
We are not associated with them.
Thank you.
I have just sent a poll around the office to vote on all the designs and hope to have the results soon.
Good luck and I hope to see all your great designs for our next project in a couple of weeks.
Morris
Hi everyone, we hope you have had a good holiday season. We will be rewarding the prizes very soon, hopefully today or tomorrow.
Thanks
Morris
We are currently going through all the designs that did not win our competition and will be contacting the designers of the designs we would like to use in our system, so please keep an eye on your inbox over the next few days.
Thank you
Morris
Target Market(s)
Beauty Salon Industry
Industry/Entity Type
Beauty Salon
Look and feel
Each slider illustrates characteristics of the customer's brand and the style your logo design should communicate.

```html
<!DOCTYPE html>
<html lang="en">
<head>
<meta charset="utf-8">
<title>Velvra – hair and urban spa</title>
<link rel="stylesheet" href="https://fonts.googleapis.com/css2?family=Arimo:wght@400;700&family=Gelasio:ital,wght@0,400;1,400;1,700&family=PT+Sans:wght@400;700&display=swap">
<style>
:root{
  --berry:#b3174f;
  --berry-dark:#8a0f3b;
  --berry-light:#d8336e;
  --ink:#333;
  --muted:#555;
  --soft:#999;
  --page:#fff;
  --mist:#f4f4f4;
  --line:#ddd;
  --charcoal:#2b2b2b;
}
*{box-sizing:border-box;margin:0;padding:0}
html,body{width:1200px;height:960px;overflow:hidden;background:var(--page)}
.page{position:relative;width:1280px;height:1024px;transform:scale(.9375);transform-origin:0 0;font-family:"Arimo",Arial,sans-serif;color:var(--ink)}
.abs{position:absolute}
.header-band{left:0;top:0;width:1280px;height:132px;background:linear-gradient(#fff,#efefef);border-bottom:1px solid #e2e2e2}
.brand{left:130px;top:22px;display:flex;align-items:flex-start;gap:10px}
.brand-dot{width:44px;height:44px;border-radius:50%;background:var(--berry)}
.brand-name{font-family:"PT Sans",sans-serif;font-size:28px;color:#8c8c8c;line-height:30px}
.brand-tag{font-family:"PT Sans",sans-serif;font-size:13px;color:#8c8c8c;margin-top:1px}
.phone{left:974px;top:18px;display:flex;align-items:center;gap:8px;font-family:"PT Sans",sans-serif;font-size:21px;color:#8c8c8c}
.pill{display:flex;align-items:center;justify-content:center;border-radius:14px;color:#fff;font-family:"PT Sans",sans-serif;font-size:14px;background:linear-gradient(var(--berry-light),var(--berry-dark));box-shadow:0 1px 2px rgba(0,0,0,.3)}
.pill.dark{background:linear-gradient(#555,#111)}
.book-top{left:1043px;top:48px;width:97px;height:25px;font-size:13px}
.ribbon-tail{top:112px;width:40px;height:44px}
.nav{left:128px;top:98px;width:1025px;height:50px;background:linear-gradient(var(--berry-light),var(--berry) 55%,var(--berry-dark));display:flex;align-items:center;padding-left:22px;box-shadow:0 3px 4px rgba(0,0,0,.2)}
.nav a{font-family:"PT Sans",sans-serif;font-size:16px;font-weight:700;color:#fff;text-decoration:none;padding:0 22px;height:50px;line-height:48px;text-shadow:0 1px 1px rgba(0,0,0,.35)}
.nav a.active{background:rgba(0,0,0,.12)}
.serif-head{font-family:"Gelasio",Georgia,serif;font-style:italic;font-size:15px;color:#444}
.intro-title{left:130px;top:185px;width:220px;text-transform:uppercase;line-height:20px;font-size:14px}
.intro-copy{left:128px;top:246px;width:228px;font-size:13px;line-height:20px;color:var(--ink)}
.intro-copy p+p{margin-top:20px}
.read-more{left:191px;top:470px;width:100px;height:27px}
.section-head{display:flex;align-items:center;gap:10px}
.section-head .hatch{flex:1;height:10px;background:repeating-linear-gradient(135deg,#ddd 0 2px,transparent 2px 4px)}
.gallery-head{left:129px;top:534px;width:224px}
.thumb{width:84px;height:72px;background:#fff;padding:3px;box-shadow:0 1px 4px rgba(0,0,0,.3)}
.thumb div{width:100%;height:100%;background:linear-gradient(135deg,#e8b997,#b57a59)}
.see-more{left:192px;top:753px;width:98px;height:27px}
.carousel{left:375px;top:189px;width:535px;height:336px;background:#fff;border:1px solid #ddd;box-shadow:0 6px 10px rgba(0,0,0,.15);padding:10px}
.carousel .slide{width:514px;height:315px;background:linear-gradient(110deg,#e9ecef 0%,#d7dbe0 25%,#c98a6c 55%,#a7604a 75%,#e4e6e9 100%)}
.arrow{top:330px;width:24px;height:36px;background:#fff;display:flex;align-items:center;justify-content:center}
.arrow.left{left:376px;border-radius:0 18px 18px 0}
.arrow.right{left:885px;border-radius:18px 0 0 18px}
.quote{left:420px;top:551px;width:444px;text-align:center;font-family:"Gelasio",Georgia,serif;font-style:italic;font-size:16px;line-height:20px;color:#777}
.quote-by{left:420px;top:605px;width:444px;text-align:center;font-family:"Gelasio",Georgia,serif;font-size:15px;color:#777}
.news-head{left:377px;top:652px;width:532px}
.news-item{top:684px;width:260px}
.news-item h3{font-size:13px;font-weight:700;color:var(--ink);margin-bottom:4px}
.news-item p{font-size:11.5px;line-height:20px;color:var(--muted)}
.news-item time{display:block;margin-top:4px;font-family:"Gelasio",Georgia,serif;font-style:italic;font-size:11px;color:#aaa}
.more-news{left:376px;top:802px;width:98px;height:27px}
.promo{left:929px;top:189px;width:223px;height:268px;background:linear-gradient(#fff,#ececec);border:1px solid #ddd}
.promo .gift{position:absolute;left:10px;top:10px;width:201px;height:120px;background:linear-gradient(#f0a800,#d8241f 55%,#b01616)}
.promo .price{position:absolute;top:138px;width:100%;text-align:center;font-family:"Gelasio",Georgia,serif;font-style:italic;font-weight:700;font-size:31px;color:var(--berry)}
.promo .offer{position:absolute;top:180px;width:100%;text-align:center;font-family:"Gelasio",Georgia,serif;font-style:italic;font-size:15px;line-height:20px;color:#555}
.promo-ribbon{left:957px;top:424px;width:169px;height:46px;background:linear-gradient(var(--berry-light),var(--berry-dark));display:flex;align-items:center;justify-content:center;font-family:"Gelasio",Georgia,serif;font-style:italic;font-size:26px;color:#fff;text-shadow:0 1px 2px rgba(0,0,0,.4)}
.addr-head{left:930px;top:501px;text-transform:uppercase;font-size:14px}
.addr{left:930px;top:532px;font-size:13px;line-height:20px;color:var(--ink)}
.map-link{left:930px;top:602px;font-family:"Gelasio",Georgia,serif;font-style:italic;font-weight:700;font-size:14px;color:var(--berry);text-decoration:none}
.hours-head{left:929px;top:653px;width:223px}
.hours{left:930px;top:686px;border-collapse:collapse;font-size:13px}
.hours td{height:18px;padding:0}
.hours td:first-child{width:106px;font-weight:700;color:#222}
.partners{left:0;top:861px;width:1280px;height:118px;background:#f6f6f6;border-top:2px dotted #ddd}
.partner{top:906px;height:42px;background:#c9c9c9;border-radius:4px}
.footer{left:0;top:979px;width:1280px;height:45px;background:linear-gradient(var(--berry),var(--berry-dark));display:flex;align-items:center;justify-content:flex-end;padding-right:138px;font-family:"PT Sans",sans-serif;font-size:13px;color:#fff}
.footer b{margin-left:3px}
.footer .sep{margin:0 15px}
</style>
</head>
<body>
<div class="page">
  <div class="abs header-band"></div>

  <div class="abs brand">
    <span class="brand-dot"></span>
    <div>
      <div class="brand-name">Velvra</div>
      <div class="brand-tag">hair and urban spa</div>
    </div>
  </div>

  <div class="abs phone">
    <svg width="14" height="20" viewBox="0 0 14 20"><path d="M10 1 L13 4 L9 8 Q6 11 9 15 L12 17 L10 19 Q2 16 3 8 Q4 3 10 1Z" fill="#b3174f"/></svg>
    070 - 5816 - 0421
  </div>
  <a class="abs pill book-top">BOOK NOW</a>

  <svg class="abs ribbon-tail" style="left:97px" viewBox="0 0 40 44"><path d="M0 0H40V44H10L22 22Z" fill="#8a0f3b"/><path d="M31 0H40V44Z" fill="#5e0827"/></svg>
  <svg class="abs ribbon-tail" style="left:1144px" viewBox="0 0 40 44"><path d="M40 0H0V44H30L18 22Z" fill="#8a0f3b"/><path d="M9 0H0V44Z" fill="#5e0827"/></svg>
  <nav class="abs nav">
    <a class="active">Home</a><a>Services</a><a>Gallery</a><a>Testimonials</a><a>News</a><a>About Us</a><a>Contact Us</a>
  </nav>

  <h2 class="abs serif-head intro-title">Let our hair and beauty skill blow you away</h2>
  <div class="abs intro-copy">
    <p>Velvra is a passionate, creative team, dedicated to delivering a second to none, personal salon experience that will ‘blow’ your mind</p>
    <p>Where ultimate hairdressing comes hand-in-hand with style, glamour, fashion, innovation and skill to create exquisite salon experience in the heart of London</p>
  </div>
  <a class="abs pill dark read-more">Read More</a>

  <div class="abs section-head gallery-head"><span class="serif-head">Gallery</span><span class="hatch"></span></div>
  <div class="abs thumb" style="left:150px;top:572px"><div role="img" aria-label="Spa massage treatment"></div></div>
  <div class="abs thumb" style="left:248px;top:572px"><div role="img" aria-label="Relaxing back massage"></div></div>
  <div class="abs thumb" style="left:150px;top:660px"><div role="img" aria-label="Hands during massage"></div></div>
  <div class="abs thumb" style="left:248px;top:657px"><div role="img" aria-label="Facial treatment"></div></div>
  <a class="abs pill see-more">See More</a>

  <div class="abs carousel"><div class="slide" role="img" aria-label="Carousel photo of a client with vivid red styled hair"></div></div>
  <div class="abs arrow left"><svg width="10" height="14"><path d="M9 0V14L0 7Z" fill="#000"/></svg></div>
  <div class="abs arrow right"><svg width="10" height="14"><path d="M1 0V14L10 7Z" fill="#000"/></svg></div>

  <blockquote class="abs quote">My hairstylist, Marisol, was truly amazing. She listened to exactly what I wanted, but also told me exactly what...</blockquote>
  <div class="abs quote-by">- Jenna Holloway -</div>

  <div class="abs section-head news-head"><span class="serif-head">Latest News &amp; Insight</span><span class="hatch"></span></div>
  <article class="abs news-item" style="left:376px">
    <h3>Book Now For Christmas</h3>
    <p>Our salon is usually very busy for the two weeks before Christmas, so please book early: call 020-5816-0421 or contact us</p>
    <time>December 4 2011</time>
  </article>
  <article class="abs news-item" style="left:655px">
    <h3>Book Now For Christmas</h3>
    <p>Our salon is usually very busy for the two weeks before Christmas, so please book early: call 020-5816-0421 or contact us</p>
    <time>December 4 2011</time>
  </article>
  <a class="abs pill more-news">More News</a>

  <div class="abs promo">
    <div class="gift" role="img" aria-label="Wrapped red gift box with green ribbon"></div>
    <div class="price">$25</div>
    <div class="offer">Complimentary gift for<br>first-time clients</div>
  </div>
  <svg class="abs" style="left:929px;top:437px" width="30" height="40" viewBox="0 0 30 40"><path d="M0 0H30V40H0L12 20Z" fill="#8a0f3b"/></svg>
  <svg class="abs" style="left:1124px;top:437px" width="30" height="40" viewBox="0 0 30 40"><path d="M30 0H0V40H30L18 20Z" fill="#8a0f3b"/></svg>
  <a class="abs promo-ribbon">Book Now</a>

  <h3 class="abs serif-head addr-head">Velvra Address :</h3>
  <address class="abs addr" style="font-style:normal">12 Linden Row<br>London<br>W2Q 7LN</address>
  <a class="abs map-link">view map</a>

  <div class="abs section-head hours-head"><span class="serif-head">Business Hours</span><span class="hatch"></span></div>
  <table class="abs hours">
    <tr><td>Monday</td><td>8:30 - 5:30</td></tr>
    <tr><td>Tuesday</td><td>8:30 - 6:00</td></tr>
    <tr><td>Wednesday</td><td>8:30 - 6:00</td></tr>
    <tr><td>Thursday</td><td>8:30 - 6:00</td></tr>
    <tr><td>Friday</td><td>8:30 - 6:00</td></tr>
    <tr><td>Saturday</td><td>7:00 - 1:00</td></tr>
    <tr><td>Sunday</td><td>Closed</td></tr>
  </table>

  <div class="abs partners"></div>
  <div class="abs partner" style="left:149px;width:151px"></div>
  <div class="abs partner" style="left:363px;width:202px"></div>
  <div class="abs partner" style="left:620px;width:296px"></div>
  <div class="abs partner" style="left:981px;width:157px"></div>

  <footer class="abs footer">Managed by <b>zQuarta</b><span class="sep">|</span><b>Admin</b></footer>
</div>
</body>
</html>
```